Small business providing disability support care requires services promotional poster

We need a digital poster to promote our services to PSAF service providers. We deliver individualised support to people living with disabilities of all ages. (Examples -Physical, intellectual, autism, hearing/vision impaired).We need the poster to highlight the services we offer - attached for convenience + group support, holiday support, camping and outdoor activities. We already have our own logo, we would like the colour theme to fit the logo aesthetic - attached. The design should communicate respect, holistic and collaborative care, fun and inclusivity.
RW Care Supports ( former name - Talvoro Vigour & Motion)

Target Market(s)

PSAF service providers (ROT, Support Coordinators, PSAF participants, Support agencies)

Industry/Entity Type

Community Services

Font styles to use
Sans Serif

Requirements
Must have
• Person centred positive imagery and language
Should not have
• Typical wheelchair or 'disabled' visuals, no puzzle pieces. Not too bright or busy - sensory overload

```html
<!DOCTYPE html>
<html lang="en">
<head>
<meta charset="utf-8">
<title>RW Care Supports – Flyers</title>
<link href="https://fonts.googleapis.com/css2?family=Montserrat:wght@300;400;500;700;800&display=swap" rel="stylesheet">
<style>
:root{
  --teal:#0f3a3c;
  --peach:#f2a383;
  --peach-deep:#e98f6c;
  --white:#ffffff;
  --ink:#0f2b2d;
  --stage:#e4e4e4;
  --photo-warm-a:#c9b8a6;
  --photo-warm-b:#8a7a6c;
  --photo-grey-a:#d9d9d9;
  --photo-grey-b:#8f8a86;
}
*{margin:0;padding:0;box-sizing:border-box}
html,body{width:1200px;height:1024px;overflow:hidden;background:var(--stage);font-family:'Montserrat',sans-serif;color:var(--ink)}
.flyer{position:absolute;width:512px;height:663px;background:var(--white);overflow:hidden}
.flyer--services{left:60px;top:115px}
.flyer--about{left:628px;top:245px}
.hero-art{position:absolute;left:0;top:0}
.brand-badge{position:absolute;left:337px;top:22px;width:134px;height:134px;border-radius:50%;background:var(--peach);display:flex;align-items:center;justify-content:center;text-align:center;font-weight:800;font-size:17px;line-height:1.15;color:var(--teal)}
.tagline-disc{position:absolute;left:238px;top:154px;width:214px;height:214px;border-radius:50%;background:var(--teal);color:var(--white)}
.tagline-disc h2{position:absolute;left:33px;top:39px;font-weight:700;font-size:20.5px;line-height:1.2;white-space:nowrap}
.tagline-disc .rule{position:absolute;left:33px;top:97px;width:41px;height:2px;background:var(--peach)}
.tagline-disc p{position:absolute;left:33px;top:105px;font-weight:300;font-size:21px;line-height:1.17;white-space:nowrap}
.service-band{position:absolute;left:146px;top:337px;width:103px;height:287px;background:var(--peach)}
.service{position:absolute;width:112px}
.service svg{display:block;width:22px;height:22px;margin-bottom:8px}
.service h3{font-weight:700;font-size:11.5px;line-height:1.2;color:var(--teal)}
.service p{font-size:10.3px;line-height:1.18;color:var(--ink)}
.service--on-band p{color:var(--white)}
.divider{position:absolute;width:27px;height:1px;background:var(--peach)}
.divider--on-band{background:var(--white)}
.footer{position:absolute;left:0;right:0;bottom:0;height:39px;background:var(--teal);display:flex;align-items:center;color:var(--white)}
.footer .name{position:absolute;left:29px;font-weight:700;font-size:14px;color:var(--peach)}
.footer .phone{position:absolute;left:187px;font-weight:700;font-size:14px;display:flex;align-items:center;gap:5px}
.footer .email{position:absolute;left:328px;font-size:9.6px;display:flex;align-items:center;gap:5px}
.footer svg{width:10px;height:10px}
.section-title{position:absolute;left:30px;top:376px;font-weight:700;font-size:14.5px;color:var(--peach);letter-spacing:.2px}
.mission-band{position:absolute;left:0;top:406px;width:370px;height:64px;background:var(--peach)}
.mission-band p{position:absolute;left:30px;top:5px;width:284px;font-size:10.2px;line-height:1.2;color:var(--white)}
.about-copy{position:absolute;left:30px;top:481px;width:284px;font-size:10.2px;line-height:1.2;color:var(--ink)}
.inset-photo{position:absolute;left:320px;top:394px;width:178px;height:178px;border-radius:50%;border:3px solid var(--white);background:radial-gradient(circle at 55% 45%,var(--photo-grey-a),var(--photo-grey-b))}
</style>
</head>
<body>

<section class="flyer flyer--services">
  <svg class="hero-art" width="512" height="663" viewBox="0 0 512 663">
    <defs>
      <radialGradient id="handsTone" cx="0.55" cy="0.5" r="0.6">
        <stop offset="0" stop-color="#cdb7a8"/><stop offset="0.6" stop-color="#a4958c"/><stop offset="1" stop-color="#6d6864"/>
      </radialGradient>
    </defs>
    <circle cx="172" cy="76" r="272" fill="url(#handsTone)" role="img" aria-label="Photo of caring hands clasped together"/>
  </svg>
  <div class="brand-badge">RW Care<br>Supports</div>
  <div class="tagline-disc">
    <h2>The best<br>Support &amp; Care</h2>
    <span class="rule"></span>
    <p>CARE. RESPECT.<br>&amp; DIGNITY AT<br>ALL TIMES</p>
  </div>

  <div class="service-band"></div>

  <div class="service" style="left:29px;top:374px">
    <svg viewBox="0 0 24 24" fill="none" stroke="#0f3a3c" stroke-width="1.4"><path d="M3 11 12 3l9 8M5 9.5V21h14V9.5M10 21v-6h4v6"/></svg>
    <h3>In-Home Care</h3>
    <p>Support with routines around school, work and medication.</p>
  </div>
  <div class="service service--on-band" style="left:153px;top:374px;width:95px">
    <svg viewBox="0 0 24 24" fill="none" stroke="#0f3a3c" stroke-width="1.4"><path d="M12 1v3M4 5l2 2M20 5l-2 2M2 12h3M19 12h3M8 14a5 5 0 1 1 8 0c-1 1-1.5 2-1.5 3h-5c0-1-.5-2-1.5-3zM9.5 20h5M10.5 23h3"/></svg>
    <h3>Individual Empowerment</h3>
    <p>Support to build capacity to become more independent</p>
  </div>
  <div class="service" style="left:270px;top:374px">
    <svg viewBox="0 0 24 24" fill="none" stroke="#0f3a3c" stroke-width="1.4"><path d="M12 2c-1 2-2 3-2 4a2 2 0 0 0 4 0c0-1-1-2-2-4zM2 15h4l5 3h6l4-3M6 15l3-2h5l-2 2M2 20h5l4 2h5"/></svg>
    <h3>Personal Care</h3>
    <p>Assistance with day to day health and hygiene care.</p>
  </div>
  <div class="service" style="left:392px;top:374px">
    <svg viewBox="0 0 24 24" fill="none" stroke="#0f3a3c" stroke-width="1.4"><path d="M2 22h20M4 22V10h5v12M9 22V4h6v18M15 22V12h5v10M11 7h2M11 10h2M11 13h2M6 13h1M6 16h1M17 15h1M17 18h1"/></svg>
    <h3>Out and About</h3>
    <p>Assistance with accessing the community.</p>
  </div>

  <span class="divider" style="left:29px;top:485px"></span>
  <span class="divider divider--on-band" style="left:153px;top:485px"></span>
  <span class="divider" style="left:270px;top:485px"></span>
  <span class="divider" style="left:392px;top:485px"></span>

  <div class="service" style="left:29px;top:502px">
    <svg viewBox="0 0 24 24" fill="none" stroke="#0f3a3c" stroke-width="1.4"><path d="M1 9l11-5 11 5-11 5zM6 11.5V17c2 2 10 2 12 0v-5.5M21 10v6"/></svg>
    <h3>Education and Employment</h3>
    <p>Learning and developing employable skills.</p>
  </div>
  <div class="service service--on-band" style="left:153px;top:502px;width:95px">
    <svg viewBox="0 0 24 24" fill="none" stroke="#0f3a3c" stroke-width="1.6"><path d="M3 12h16M13 6l6 6-6 6"/></svg>
    <h3>Transport</h3>
    <p>Assistance to get from A to B.</p>
  </div>
  <div class="service" style="left:270px;top:502px">
    <svg viewBox="0 0 24 24" fill="none" stroke="#0f3a3c" stroke-width="1.4"><path d="M2 10v4M5 7v10M8 8v8M8 12h8M16 8v8M19 7v10M22 10v4"/></svg>
    <h3>Personal Training</h3>
    <p>Improving Fitness with participants.</p>
  </div>

  <footer class="footer">
    <span class="name">RW Care Supports</span>
    <span class="phone"><svg viewBox="0 0 24 24" fill="none" stroke="#f2a383" stroke-width="2"><path d="M5 3h4l2 5-3 2a12 12 0 0 0 6 6l2-3 5 2v4a2 2 0 0 1-2 2A18 18 0 0 1 3 5a2 2 0 0 1 2-2z"/></svg>0400 218 604</span>
    <span class="email"><svg viewBox="0 0 24 24" fill="none" stroke="#f2a383" stroke-width="2"><rect x="2" y="5" width="20" height="14"/><path d="M2 5l10 8 10-8"/></svg>hello@rwcaresupports.com.au</span>
  </footer>
</section>

<section class="flyer flyer--about">
  <svg class="hero-art" width="512" height="663" viewBox="0 0 512 663">
    <defs>
      <radialGradient id="familyTone" cx="0.55" cy="0.45" r="0.6">
        <stop offset="0" stop-color="#c98a64"/><stop offset="0.55" stop-color="#a06a4c"/><stop offset="1" stop-color="#6f5647"/>
      </radialGradient>
    </defs>
    <circle cx="195" cy="102" r="246" fill="url(#familyTone)" role="img" aria-label="Photo of a carer and a young person looking at a tablet together"/>
  </svg>
  <div class="brand-badge">RW Care<br>Supports</div>
  <div class="tagline-disc">
    <h2>The best<br>Support &amp; Care</h2>
    <span class="rule"></span>
    <p>CARE. RESPECT.<br>&amp; DIGNITY AT<br>ALL TIMES</p>
  </div>

  <h2 class="section-title">VISION, MISSION &amp; VALUES</h2>
  <div class="mission-band">
    <p>Delivering person centered supports to individuals living with disabilities to support, empower and build the capacity of every person aligned with RW Care Supports. Delivering honest, holistic and reliable care.</p>
  </div>
  <p class="about-copy">RW CARE SUPPORTS Is a sole trading business which provides individualised support services to Participants on the PSAF – Personal Support Assistance Fund. Supports delivered will be dependent on each individuals goals, capacity, PSAF funding and expected outcomes.</p>
  <div class="inset-photo" role="img" aria-label="Photo of caring hands clasped together"></div>

  <footer class="footer">
    <span class="name">RW Care Supports</span>
    <span class="phone"><svg viewBox="0 0 24 24" fill="none" stroke="#f2a383" stroke-width="2"><path d="M5 3h4l2 5-3 2a12 12 0 0 0 6 6l2-3 5 2v4a2 2 0 0 1-2 2A18 18 0 0 1 3 5a2 2 0 0 1 2-2z"/></svg>0400 218 604</span>
    <span class="email"><svg viewBox="0 0 24 24" fill="none" stroke="#f2a383" stroke-width="2"><rect x="2" y="5" width="20" height="14"/><path d="M2 5l10 8 10-8"/></svg>hello@rwcaresupports.com.au</span>
  </footer>
</section>

</body>
</html>
```